Unique and original Business Card for Financial Services Business

I have moved premises and need to change the detail on my business card so thought now is a good time for a re-design. Looking for something professional and modern with colours to fit in with out logo. Like the idea of foil or embossing if that works but not a must have but I do want something that stands out and that I could not design myself.

Once business card is designed I will also be looking to get letterhead and flyers done but want the business card concept in place first.

The majority of designs I am receiving are generic and template based. I am looking for something unique and original. We have some great design elements in our logo, think outside the box and show me something that stands out from the crowd.

Target Market(s)

Business Professionals

Industry/Entity Type

Finance

Contact Information for Business Card

Name: Delphine Moore Phone 0438 297 614 Address PO Box 7816 Ashvale NSW 2411 Email info@tidewellmoneyservices.example.com.au website www.tidewellmoneyservices.example.com.au

Font styles to use
Other font styles liked:
• Ralway

Requirements
Should not have
• No black backgrounds please

```html
<!DOCTYPE html>
<html lang="en">
<head>
<meta charset="utf-8">
<title>Tidewell Money Services – Business Card</title>
<link rel="stylesheet" href="https://fonts.googleapis.com/css2?family=Raleway:wght@300;400;700&display=swap">
<style>
  :root {
    --backdrop: #6e6e6d;
    --card-white: #ffffff;
    --teal: #0a9e9a;
    --navy: #0b4f6c;
    --brand: #1b7f92;
    --ink-light: #ffffff;
  }
  html, body {
    margin: 0;
    padding: 0;
    width: 1200px;
    height: 801px;
    overflow: hidden;
    background: var(--backdrop);
    font-family: "Raleway", sans-serif;
  }
  .canvas {
    position: relative;
    width: 1200px;
    height: 801px;
  }
  .card {
    position: absolute;
    top: 245px;
    width: 540px;
    height: 310px;
    border-radius: 16px;
    overflow: hidden;
    background: var(--card-white);
    box-shadow: 0 10px 28px rgba(0,0,0,0.35);
  }
  .card--contact { left: 40px; }
  .card--brand {
    left: 620px;
    border-bottom: 4px solid var(--teal);
    height: 306px;
  }
  .card__swoosh {
    position: absolute;
    inset: 0;
  }
  .wordmark {
    position: absolute;
    color: var(--brand);
    font-weight: 300;
    line-height: 1;
    display: flex;
    align-items: center;
  }
  .wordmark__dot {
    border-radius: 50%;
    background: var(--brand);
    flex: none;
  }
  .wordmark__lines { display: flex; flex-direction: column; }
  .card--contact .wordmark {
    right: 40px;
    top: 42px;
    gap: 10px;
  }
  .card--contact .wordmark__dot { width: 34px; height: 34px; }
  .card--contact .wordmark__name { font-size: 28px; letter-spacing: 1px; }
  .card--contact .wordmark__tag { font-size: 14px; letter-spacing: 5px; margin-top: 5px; }

  .card--brand .wordmark {
    left: 50%;
    top: 50%;
    transform: translate(-50%, -50%);
    gap: 18px;
  }
  .card--brand .wordmark__dot { width: 70px; height: 70px; }
  .card--brand .wordmark__name { font-size: 54px; letter-spacing: 2px; }
  .card--brand .wordmark__tag { font-size: 24px; letter-spacing: 10px; margin-top: 10px; }

  .contact {
    position: absolute;
    left: 32px;
    top: 168px;
    color: var(--ink-light);
  }
  .contact__name {
    margin: 0 0 12px;
    font-size: 22px;
    font-weight: 700;
  }
  .contact__list {
    list-style: none;
    margin: 0;
    padding: 0;
    font-size: 12px;
  }
  .contact__item {
    display: flex;
    align-items: center;
    gap: 9px;
    margin-bottom: 7px;
  }
  .contact__icon {
    width: 12px;
    height: 12px;
    flex: none;
    fill: var(--ink-light);
  }
</style>
</head>
<body>
<main class="canvas">

  <section class="card card--contact" aria-label="Business card, contact side">
    <svg class="card__swoosh" viewBox="0 0 540 310" width="540" height="310" aria-hidden="true">
      <path d="M120 0 C230 205 410 215 540 40 L540 310 L0 310 L0 0 Z" fill="var(--navy)"/>
      <path d="M150 0 C255 215 420 225 540 62 L540 310 L0 310 L0 0 Z" fill="#ffffff"/>
      <path d="M152 0 C258 223 424 232 540 70 L540 310 L0 310 L0 0 Z" fill="var(--teal)"/>
      <path d="M0 0 L150 0 C255 215 420 225 540 62 L540 0 Z" fill="#ffffff"/>
      <path d="M0 0 L120 0 C230 205 410 215 540 40 L540 0 Z" fill="#ffffff"/>
      <path d="M120 0 C230 205 410 215 540 40 L540 55 C410 225 245 222 138 0 Z" fill="var(--navy)"/>
      <path d="M0 0 H125 C128 6 131 12 134 18 C90 120 40 170 0 185 Z" fill="#ffffff"/>
    </svg>

    <div class="wordmark">
      <span class="wordmark__dot"></span>
      <span class="wordmark__lines">
        <span class="wordmark__name">TIDEWELL</span>
        <span class="wordmark__tag">Money Services</span>
      </span>
    </div>

    <div class="contact">
      <h1 class="contact__name">Delphine Moore</h1>
      <ul class="contact__list">
        <li class="contact__item">
          <svg class="contact__icon" viewBox="0 0 12 12" aria-hidden="true"><path d="M6 0a4 4 0 0 0-4 4c0 3 4 8 4 8s4-5 4-8a4 4 0 0 0-4-4zm0 5.5A1.5 1.5 0 1 1 6 2.5a1.5 1.5 0 0 1 0 3z"/></svg>
          <span>PO Box 7816 Ashvale NSW 2411</span>
        </li>
        <li class="contact__item">
          <svg class="contact__icon" viewBox="0 0 12 12" aria-hidden="true"><path d="M2.5 0.5l2 2.5-1.2 1.3c.7 1.6 2 2.9 3.6 3.6L8.2 6.7l2.6 2-1 2.6C5 11 1 7 0.7 2.2z"/></svg>
          <span>0438 297 614</span>
        </li>
        <li class="contact__item">
          <svg class="contact__icon" viewBox="0 0 12 12" aria-hidden="true"><path d="M0 2h12v8H0zM1 3l5 3.6L11 3v-.2H1z" fill-rule="evenodd"/></svg>
          <span>info@tidewellmoneyservices.example.com.au</span>
        </li>
        <li class="contact__item">
          <svg class="contact__icon" viewBox="0 0 12 12" aria-hidden="true"><circle cx="6" cy="6" r="5.5"/><path d="M0.5 6h11M6 0.5c-2.2 2.8-2.2 8.2 0 11M6 0.5c2.2 2.8 2.2 8.2 0 11" stroke="var(--teal)" stroke-width="0.9" fill="none"/></svg>
          <span>www.tidewellmoneyservices.example.com.au</span>
        </li>
      </ul>
    </div>
  </section>

  <section class="card card--brand" aria-label="Business card, brand side">
    <div class="wordmark">
      <span class="wordmark__dot"></span>
      <span class="wordmark__lines">
        <span class="wordmark__name">TIDEWELL</span>
        <span class="wordmark__tag">Money Services</span>
      </span>
    </div>
  </section>

</main>
</body>
</html>
```